ZENITH conference Slide Deck

This is a conference for our team that will be 3 days of discussions on how to build our business in the middle of these challenging time. Its a bit of a battle and so we are going with a red and grey/black these although I am open to your interpretation. I will include a few graphics that we have started on to show you the look. But I am just getting started, INSPIRE ME! The screen will be 100' across the front of the room and these decks will show on each side and I will reformat for the middle 1X6 screen as needed. I have the AI file of the logo if you need it. I don't see where to upload it here.

Target Market(s)

our top producers

Industry/Entity Type

Real Estate Agent

Font styles to use
Sans Serif

Colors
ec1f27

Requirements
Must have
• Depth, creativity

```html
<!DOCTYPE html>
<html lang="en">
<head>
<meta charset="utf-8">
<title>ZENITH Master Slide Presentation</title>
<link rel="stylesheet" href="https://fonts.googleapis.com/css2?family=Poppins:wght@400;500;600;700;800&display=swap">
<style>
:root{
  --red:#ec1f27;
  --black:#0d0d0d;
  --ink:#222222;
  --grey:#8e8e8e;
  --mid:#b5b5b5;
  --light:#ececec;
  --page:#efefef;
  --white:#ffffff;
}
*{box-sizing:border-box;margin:0;padding:0}
html,body{width:1200px;height:3137px;overflow:hidden;background:var(--page)}
body{font-family:"Poppins",sans-serif;color:var(--ink)}
.deck{display:grid;grid-template-columns:555px 555px;grid-auto-rows:312px;column-gap:33px;row-gap:32.7px;padding:29px 29px 0 28px}
.slide{position:relative;overflow:hidden;background:var(--white);box-shadow:0 6px 14px rgba(0,0,0,.18)}
.slide > *{position:absolute}
.hdr{left:0;top:0;width:555px;height:312px}
.hdr-title{left:52px;top:14px;color:var(--white);font-weight:700;font-size:17px;letter-spacing:.3px}
.brand{font-weight:800;color:var(--red);letter-spacing:1px;line-height:1}
.photo{background:linear-gradient(135deg,#d9d9d9,#8a8a8a)}
.photo-light{background:linear-gradient(135deg,#fafafa,#dedede)}
.body{font-size:6px;line-height:15px;color:#444;text-align:justify}
.tiny{font-size:5.5px;line-height:9px;color:var(--grey)}
.label{font-size:7.5px;font-weight:600;color:var(--ink)}
.red{color:var(--red)}
.social{display:flex;gap:3px}
.social span{width:10px;height:10px;border:1px solid currentColor;border-radius:50%}
.card{background:var(--white);border-radius:18px;box-shadow:0 4px 12px rgba(0,0,0,.18)}
.center{text-align:center}
.bar-track{height:5px;background:var(--light);border-radius:3px}
.bar-fill{height:5px;border-radius:3px;background:var(--red)}
.pill{border:1px solid var(--ink);border-radius:10px;font-size:7px;font-weight:600;text-align:center;line-height:16px;box-shadow:0 2px 5px rgba(0,0,0,.2)}
.mgmt-box{border-radius:7px;font-size:7.5px;text-align:center;box-shadow:0 3px 7px rgba(0,0,0,.18)}
.badge{background:var(--white);border-radius:6px;box-shadow:0 3px 8px rgba(0,0,0,.2)}
.badge i{position:absolute;left:14px;right:14px;top:10px;bottom:10px;background:#c9c9c9;border-radius:4px}
.stars{color:var(--red);font-size:8px;letter-spacing:1px}
.contact{display:flex;align-items:center;gap:12px;color:var(--white);font-size:8px}
</style>
</head>
<body>
<main class="deck">

<!-- 1 title -->
<section class="slide">
  <div class="photo-light" role="img" aria-label="Faded photo of hands working on a laptop" style="left:0;top:0;width:555px;height:312px"></div>
  <svg class="hdr" viewBox="0 0 555 312"><path d="M0 0H555V45C545 75 530 85 505 85H0Z" fill="var(--black)"/><path d="M0 45H505C530 45 545 55 555 80V0Z" fill="var(--black)"/></svg>
  <svg class="hdr" viewBox="0 0 555 312"><path d="M0 0H555V35C548 70 525 88 500 88H0Z" fill="var(--white)" opacity="0"/></svg>
  <div class="brand" style="left:0;width:555px;top:20px;text-align:center;font-size:26px">ZENITH</div>
  <div style="left:0;width:555px;top:116px;text-align:center;font-size:7px;letter-spacing:4px;color:var(--ink)">www.yourwebsite.com</div>
  <div style="left:0;width:555px;top:144px;text-align:center;font-size:21px;font-weight:700;color:var(--black)"><span class="red">ZENITH</span> MASTER SLIDE PRESENTATION</div>
  <div class="pill" style="left:207px;top:212px;width:141px;background:var(--white)">PRESENTER NAME</div>
  <div class="red" style="left:0;width:555px;top:258px;text-align:center;font-size:9px;font-weight:700">2020</div>
  <div class="social" style="left:260px;top:286px;color:var(--ink)"><span></span><span></span><span></span></div>
</section>

<!-- 2 cover -->
<section class="slide" style="background:var(--black)">
  <svg class="hdr" viewBox="0 0 555 312"><path d="M0 0H170C140 0 120 20 120 50V312H0Z" fill="var(--red)"/><path d="M124 312V52C124 22 144 4 174 4" stroke="var(--white)" stroke-width="3" fill="none"/></svg>
  <div class="photo" role="img" aria-label="Black and white photo of an arched white corridor" style="left:43px;top:67px;width:160px;height:199px;border-radius:26px"></div>
  <div style="right:24px;top:52px;text-align:right;color:var(--white);font-weight:700;font-size:23px;line-height:26px">MASTER SLIDE<br>PRESENTATION</div>
  <div style="right:24px;top:112px;color:var(--white);font-size:7px;letter-spacing:4px">SUBTITLE GOES HERE</div>
  <div class="social" style="right:24px;top:130px;color:var(--white)"><span></span><span></span><span></span></div>
  <div class="brand" style="right:28px;top:248px;font-size:30px">ZENITH</div>
</section>

<!-- 3 about -->
<section class="slide">
  <svg class="hdr" viewBox="0 0 555 312"><path d="M0 0H490C482 32 468 50 440 50H50C20 50 0 70 0 100Z" fill="var(--black)"/></svg>
  <div class="hdr-title">ABOUT US</div>
  <svg style="left:33px;top:100px" width="22" height="22" viewBox="0 0 22 22"><path d="M2 11L11 3L20 11" stroke="var(--red)" stroke-width="2.5" fill="none"/><rect x="5" y="10" width="12" height="10" fill="var(--red)"/><rect x="9" y="14" width="4" height="6" fill="var(--white)"/></svg>
  <p class="body" style="left:34px;top:130px;width:204px">Lorem ipsum dolor sit amet, consectetuer adipiscing elit, sed diam nonummy nibh euismod tincidunt ut laoreet dolore magna aliquam erat volutpat. Ut wisi enim ad minim veniam, quis nostrud exerci tation ullamcorper suscipit lobortis nisl ut aliquip ex ea commodo consequat. Duis autem vel eum iriure dolor in hendrerit in vulputate velit esse molestie consequat, vel illum dolore eu feugiat nulla facilisis at vero eros et accumsan et iusto odio dignissim qui blandit praesent luptatum zzril delenit augue duis dolore te feugait nulla facilisi.</p>
  <div class="photo" role="img" aria-label="Black and white photo of a modern house" style="left:274px;top:71px;width:281px;height:241px;border-top-left-radius:60px"></div>
</section>

<!-- 4 roadmap -->
<section class="slide">
  <svg class="hdr" viewBox="0 0 555 312"><path d="M0 0H490C482 32 468 50 440 50H50C20 50 0 70 0 100Z" fill="var(--black)"/>
    <line x1="97" y1="189" x2="515" y2="189" stroke="var(--grey)" stroke-dasharray="2 2"/>
    <line x1="97" y1="152" x2="97" y2="172" stroke="var(--grey)" stroke-dasharray="2 2"/>
    <line x1="318" y1="152" x2="318" y2="172" stroke="var(--grey)" stroke-dasharray="2 2"/>
    <line x1="207" y1="206" x2="207" y2="232" stroke="var(--grey)" stroke-dasharray="2 2"/>
    <line x1="429" y1="206" x2="429" y2="232" stroke="var(--grey)" stroke-dasharray="2 2"/>
    <g font-family="Poppins,sans-serif" font-size="8" font-weight="700" text-anchor="middle">
      <circle cx="97" cy="189" r="18" fill="var(--white)" stroke="#cfcfcf" stroke-width="5"/><text x="97" y="192">2018</text>
      <circle cx="207" cy="189" r="18" fill="var(--white)" stroke="var(--red)" stroke-width="5"/><text x="207" y="192">2019</text>
      <circle cx="318" cy="189" r="18" fill="var(--white)" stroke="#cfcfcf" stroke-width="5"/><text x="318" y="192">2020</text>
      <circle cx="429" cy="189" r="18" fill="var(--white)" stroke="var(--red)" stroke-width="5"/><text x="429" y="192">2021</text>
    </g></svg>
  <div class="hdr-title">OUR ROADMAP</div>
  <div class="tiny center" style="left:37px;top:86px;width:130px">sit amet, consectetuer adipiscing elit, sed diam nonummy nibh euismod tincidunt</div>
  <div class="label center" style="left:37px;top:107px;width:130px">LOREM IPSUM DOLOR</div>
  <div class="tiny center" style="left:258px;top:86px;width:130px">sit amet, consectetuer adipiscing elit, sed diam nonummy nibh euismod tincidunt</div>
  <div class="label center" style="left:258px;top:107px;width:130px">LOREM IPSUM DOLOR</div>
  <div class="label center red" style="left:142px;top:244px;width:130px">LOREM IPSUM DOLOR</div>
  <div class="tiny center" style="left:142px;top:257px;width:130px">sit amet, consectetuer adipiscing elit, sed diam nonummy nibh euismod tincidunt</div>
  <div class="label center red" style="left:364px;top:244px;width:130px">LOREM IPSUM DOLOR</div>
  <div class="tiny center" style="left:364px;top:257px;width:130px">sit amet, consectetuer adipiscing elit, sed diam nonummy nibh euismod tincidunt</div>
</section>

<!-- 5 vision -->
<section class="slide">
  <svg class="hdr" viewBox="0 0 555 312"><path d="M0 0H490C482 32 468 50 440 50H50C20 50 0 70 0 100Z" fill="var(--black)"/></svg>
  <div class="hdr-title">OUR VISION, VALUE &amp; GOAL</div>
  <div class="card" style="left:46px;top:117px;width:134px;height:157px"></div>
  <div class="card" style="left:211px;top:117px;width:134px;height:157px"></div>
  <div class="card" style="left:375px;top:117px;width:134px;height:157px"></div>
  <svg class="hdr" viewBox="0 0 555 312">
    <g stroke="var(--white)" stroke-width="3">
      <polygon points="113,94 133,105 133,128 113,139 93,128 93,105" fill="var(--red)"/>
      <polygon points="278,94 298,105 298,128 278,139 258,128 258,105" fill="var(--black)"/>
      <polygon points="442,94 462,105 462,128 442,139 422,128 422,105" fill="#9a9a9a"/>
    </g>
    <g fill="none" stroke="var(--white)" stroke-width="1.5">
      <ellipse cx="113" cy="117" rx="9" ry="5"/><circle cx="113" cy="117" r="2.5"/>
      <circle cx="278" cy="117" r="8"/><circle cx="278" cy="117" r="4"/><line x1="278" y1="117" x2="287" y2="108"/>
      <circle cx="442" cy="117" r="7"/><line x1="442" y1="106" x2="442" y2="128"/><line x1="431" y1="117" x2="453" y2="117"/>
    </g>
    <g stroke="#666" stroke-dasharray="1.5 2"><line x1="57" y1="150" x2="57" y2="258"/><line x1="222" y1="150" x2="222" y2="258"/><line x1="386" y1="150" x2="386" y2="258"/></g>
  </svg>
  <div class="center red" style="left:46px;top:143px;width:134px;font-size:10px;font-weight:600">Lorem ipsum</div>
  <div class="center" style="left:211px;top:145px;width:134px;font-size:10px;font-weight:600;color:var(--black)">Lorem ipsum</div>
  <div class="center" style="left:375px;top:143px;width:134px;font-size:10px;font-weight:600;color:var(--grey)">Lorem ipsum</div>
  <div class="tiny center" style="left:66px;top:171px;width:94px">Lorem ipsum dolor sit amet, consectetuer adipiscing elit, sed diam nonummy nibh euismod tincidunt ut laoreet dolore magna aliquam erat volutpat.</div>
  <div class="tiny center" style="left:231px;top:171px;width:94px">Lorem ipsum dolor sit amet, consectetuer adipiscing elit, sed diam nonummy nibh euismod tincidunt ut laoreet dolore magna aliquam erat volutpat.</div>
  <div class="tiny center" style="left:395px;top:171px;width:94px">Lorem ipsum dolor sit amet, consectetuer adipiscing elit, sed diam nonummy nibh euismod tincidunt ut laoreet dolore magna aliquam erat volutpat.</div>
</section>

<!-- 6 testimonials -->
<section class="slide">
  <svg class="hdr" viewBox="0 0 555 312"><path d="M0 0H460C452 32 438 50 410 50H180C140 50 120 70 120 100V312H0Z" fill="var(--black)"/>
    <g stroke="var(--grey)" fill="none"><path d="M180 91H442Q452 91 452 101V107"/><path d="M180 119H340Q350 119 350 129V134"/><path d="M180 146H223Q233 146 233 156V161"/></g>
    <g fill="var(--ink)" stroke="var(--white)" stroke-width="2"><circle cx="180" cy="91" r="6"/><circle cx="180" cy="119" r="6"/><circle cx="180" cy="146" r="6"/></g></svg>
  <div style="left:46px;top:79px;width:120px;height:177px;background:var(--red);border-radius:18px;color:var(--white);padding:14px">
    <div style="font-size:20px;font-weight:700;line-height:24px;text-align:center">Title<br>Slide</div>
    <div style="font-size:6.5px;text-align:center;margin-top:4px">(Testimonials)</div>
    <div style="font-size:6px;font-weight:600;line-height:11px;margin-top:18px">Lorem Ipsum is simply dummy text of the printing and typesetting industry</div></div>
  <div class="card" style="left:192px;top:161px;width:83px;height:131px;border-radius:8px;padding:10px 8px"><div class="tiny" style="line-height:14px">Lorem ipsum is simply dummy text of the printing and typesetting industry</div><div class="stars" style="margin-top:6px">★★★★★</div></div>
  <div style="left:192px;top:270px;width:83px;height:22px;background:var(--red);border-radius:0 0 8px 8px;color:var(--white);font-size:7.5px;text-align:center;line-height:22px">Lorem Ipsum</div>
  <div class="card" style="left:312px;top:134px;width:83px;height:134px;border-radius:8px;padding:10px 8px"><div class="tiny" style="line-height:14px">Lorem ipsum is simply dummy text of the printing and typesetting industry</div><div class="stars" style="margin-top:6px">★★★★★</div></div>
  <div style="left:312px;top:246px;width:83px;height:22px;background:var(--red);border-radius:0 0 8px 8px;color:var(--white);font-size:7.5px;text-align:center;line-height:22px">Lorem Ipsum</div>
  <div class="card" style="left:424px;top:107px;width:80px;height:134px;border-radius:8px;padding:10px 8px"><div class="tiny" style="line-height:14px">Lorem ipsum is simply dummy text of the printing and typesetting industry</div><div class="stars" style="margin-top:6px">★★★★★</div></div>
  <div style="left:424px;top:219px;width:80px;height:22px;background:var(--red);border-radius:0 0 8px 8px;color:var(--white);font-size:7.5px;text-align:center;line-height:22px">Lorem Ipsum</div>
</section>

<!-- 7 infographic -->
<section class="slide">
  <svg class="hdr" viewBox="0 0 555 312"><path d="M0 0H490C482 32 468 50 440 50H50C20 50 0 70 0 100Z" fill="var(--black)"/>
    <circle cx="77" cy="134" r="34" fill="var(--white)" stroke="var(--light)" stroke-width="6"/>
    <circle cx="77" cy="134" r="34" fill="none" stroke="var(--red)" stroke-width="6" stroke-dasharray="156 214" transform="rotate(-90 77 134)"/>
    <circle cx="77" cy="229" r="34" fill="var(--white)" stroke="var(--light)" stroke-width="6"/>
    <circle cx="77" cy="229" r="34" fill="none" stroke="var(--black)" stroke-width="6" stroke-dasharray="107 214" transform="rotate(-90 77 229)"/>
    <g font-family="Poppins,sans-serif" font-weight="700" text-anchor="middle" font-size="20"><text x="77" y="141" fill="var(--red)">73%</text><text x="77" y="236" fill="var(--black)">50%</text></g></svg>
  <div class="hdr-title">INFOGRAPHIC</div>
  <div class="label red" style="left:131px;top:112px;font-size:7px">PROJECT 01</div>
  <div class="tiny" style="left:131px;top:125px;width:100px;line-height:11px">Lorem Ipsum is simply dummy text of the printing and typesetting industry</div>
  <div class="label" style="left:131px;top:207px;font-size:7px">PROJECT 02</div>
  <div class="tiny" style="left:131px;top:220px;width:100px;line-height:11px">Lorem Ipsum is simply dummy text of the printing and typesetting industry</div>
  <div style="left:270px;top:108px;width:232px">
    <div class="label" style="font-size:7px;display:flex;justify-content:space-between">PROJECT 03<span style="color:var(--grey);font-weight:400">32%</span></div>
    <div class="bar-track" style="margin:3px 0 19px"><div class="bar-fill" style="width:32%"></div></div>
    <div class="label" style="font-size:7px;display:flex;justify-content:space-between">PROJECT 04<span style="color:var(--grey);font-weight:400">72%</span></div>
    <div class="bar-track" style="margin:3px 0 19px"><div class="bar-fill" style="width:72%;background:var(--black)"></div></div>
    <div class="label" style="font-size:7px;display:flex;justify-content:space-between">PROJECT 05<span style="color:var(--grey);font-weight:400">52%</span></div>
    <div class="bar-track" style="margin:3px 0 19px"><div class="bar-fill" style="width:52%"></div></div>
    <div class="label" style="font-size:7px;display:flex;justify-content:space-between">PROJECT 06<span style="color:var(--grey);font-weight:400">12%</span></div>
    <div class="bar-track" style="margin:3px 0 19px"><div class="bar-fill" style="width:12%;background:var(--black)"></div></div>
    <div class="label" style="font-size:7px;display:flex;justify-content:space-between">PROJECT 07<span style="color:var(--grey);font-weight:400">60%</span></div>
    <div class="bar-track" style="margin-top:3px"><div class="bar-fill" style="width:60%"></div></div>
  </div>
</section>

<!-- 8 mission -->
<section class="slide">
  <div class="photo" role="img" aria-label="Black and white photo of a modern bedroom interior" style="left:0;top:0;width:555px;height:150px"></div>
  <svg class="hdr" viewBox="0 0 555 312"><path d="M0 144H122V312H0Z" fill="var(--black)"/><path d="M122 312V190C122 160 140 144 170 144H555V312Z" fill="var(--white)"/></svg>
  <div class="brand" style="right:8px;top:114px;font-size:26px">ZENITH</div>
  <div style="left:21px;top:186px;color:var(--white);font-weight:700;font-size:17px;line-height:20px">OUR<br>MISSION</div>
  <p class="body" style="left:168px;top:175px;width:356px;line-height:14.5px">Lorem ipsum dolor sit amet, consectetuer adipiscing elit, sed diam nonummy nibh euismod tincidunt ut laoreet dolore magna aliquam erat volutpat. Ut wisi enim ad minim veniam, quis nostrud exerci tation ullamcorper suscipit lobortis nisl ut aliquip ex ea commodo consequat. Duis autem vel eum iriure dolor in hendrerit in vulputate velit esse molestie consequat, vel illum dolore eu feugiat nulla facilisis at vero eros et accumsan et iusto odio dignissim qui blandit praesent luptatum zzril delenit augue duis dolore te feugait nulla facilisi.</p>
</section>

<!-- 9 founders -->
<section class="slide">
  <svg class="hdr" viewBox="0 0 555 312"><path d="M0 0H490C482 32 468 50 440 50H50C20 50 0 70 0 100Z" fill="var(--black)"/></svg>
  <div class="hdr-title">OUR FOUNDERS</div>
  <div class="photo" role="img" aria-label="Black and white portrait photo of the founder" style="left:43px;top:85px;width:119px;height:181px"></div>
  <div class="brand" style="left:43px;top:244px;width:119px;text-align:center;font-size:20px">ZENITH</div>
  <div style="left:185px;top:112px;font-weight:700;font-size:12px;color:var(--black)">NAME</div>
  <div style="left:185px;top:130px;font-size:6.5px;letter-spacing:3px;font-weight:600">FOUNDER/CEO</div>
  <div class="brand" style="left:408px;top:112px;font-size:24px;color:#e6e6e6">ZENITH</div>
  <p class="body" style="left:185px;top:149px;width:317px;line-height:16.5px">Lorem ipsum dolor sit amet, consectetuer adipiscing elit, sed diam nonummy nibh euismod tincidunt ut laoreet dolore magna aliquam erat volutpat. Ut wisi enim ad minim veniam, quis nostrud exerci tation ullamcorper suscipit lobortis nisl ut aliquip ex ea commodo consequat. Duis autem vel eum iriure dolor in hendrerit in vulputate velit esse molestie consequat, vel illum dolore eu feugiat nulla facilisis at vero eros et accumsan et iusto odio dignissim qui blandit praesent luptatum zzril delenit augue duis dolore te feugait nulla facilisi.</p>
</section>

<!-- 10 team -->
<section class="slide" style="background:var(--black)">
  <svg class="hdr" viewBox="0 0 555 312"><path d="M0 312V200C0 160 25 140 65 140H490C530 140 555 125 555 100V312Z" fill="var(--white)"/>
    <g fill="none" stroke="var(--red)" stroke-width="6"><path d="M71 144A46 46 0 0 1 163 144"/><path d="M229 144A46 46 0 0 1 321 144"/><path d="M385 144A46 46 0 0 1 477 144"/></g></svg>
  <div style="left:0;width:555px;top:17px;text-align:center;color:var(--white);font-weight:700;font-size:16px">OUR TEAM</div>
  <div style="left:255px;top:44px;width:45px;height:2px;background:var(--white)"></div>
  <div class="photo" role="img" aria-label="Black and white portrait of a team member" style="left:75px;top:102px;width:84px;height:84px;border-radius:50%"></div>
  <div class="photo" role="img" aria-label="Black and white portrait of a team member" style="left:233px;top:102px;width:84px;height:84px;border-radius:50%"></div>
  <div class="photo" role="img" aria-label="Black and white portrait of a team member" style="left:389px;top:102px;width:84px;height:84px;border-radius:50%"></div>
  <div class="center" style="left:47px;top:203px;width:140px"><div style="font-size:8px;font-weight:700">NAME</div><div style="font-size:6.5px;letter-spacing:3px;margin-top:2px">POTITION</div><div style="font-size:6.5px;line-height:12px;margin-top:8px;color:#444">Lorem ipsum dolor sit amet, consectetuer adipiscing elit, sed diam nonummy nibh</div></div>
  <div class="center red" style="left:205px;top:203px;width:140px"><div style="font-size:8px;font-weight:700">NAME</div><div style="font-size:6.5px;letter-spacing:3px;margin-top:2px">POTITION</div><div style="font-size:6.5px;line-height:12px;margin-top:8px">Lorem ipsum dolor sit amet, consectetuer adipiscing elit, sed diam nonummy nibh</div></div>
  <div class="center" style="left:361px;top:203px;width:140px;color:var(--grey)"><div style="font-size:8px;font-weight:700">NAME</div><div style="font-size:6.5px;letter-spacing:3px;margin-top:2px">POTITION</div><div style="font-size:6.5px;line-height:12px;margin-top:8px">Lorem ipsum dolor sit amet, consectetuer adipiscing elit, sed diam nonummy nibh</div></div>
</section>

<!-- 11 projects -->
<section class="slide">
  <div class="photo" role="img" aria-label="Black and white photo of a suburban house" style="left:0;top:0;width:230px;height:312px"></div>
  <svg class="hdr" viewBox="0 0 555 312"><path d="M110 0A180 180 0 0 1 110 312H555V0Z" fill="var(--white)"/><path d="M110 0A180 180 0 0 1 110 312" fill="none" stroke="var(--black)" stroke-width="26" transform="translate(-14 0)"/>
    <g stroke="var(--white)" stroke-width="3" fill="var(--red)">
      <polygon points="306,12 326,23 326,45 306,56 286,45 286,23"/>
      <polygon points="336,84 356,95 356,117 336,128 316,117 316,95"/>
      <polygon points="336,155 356,166 356,188 336,199 316,188 316,166" fill="#9a9a9a"/>
      <polygon points="306,228 326,239 326,261 306,272 286,261 286,239"/></g>
    <g fill="none" stroke="var(--white)" stroke-width="1.5"><path d="M298 30L306 26L314 30L306 34Z M298 36L306 40L314 36"/><path d="M330 114L336 98L342 114M332 108H340"/><rect x="329" y="170" width="14" height="12"/><path d="M299 258V244H304V258M306 258V248H311V258"/></g>
    <path d="M306 0V12M306 272V290M306 56L336 84M336 128V155M336 199L306 228" stroke="#999" stroke-dasharray="2 2"/></svg>
  <div style="left:46px;top:135px;color:var(--white);font-weight:700;font-size:20px;line-height:26px">OUR<br>PROJECTS</div>
  <svg style="left:46px;top:190px" width="24" height="24" viewBox="0 0 24 24" fill="none" stroke="var(--white)" stroke-width="1.5"><circle cx="12" cy="12" r="10"/><circle cx="12" cy="9" r="5"/><circle cx="9" cy="14" r="5"/><circle cx="15" cy="14" r="5"/></svg>
  <div style="left:346px;top:22px"><div style="font-size:10px;font-weight:500">Lorem ipsum</div><div class="tiny" style="width:120px">Lorem ipsum dolor sit amet, consectetuer adipiscing elit.</div></div>
  <div style="left:376px;top:94px"><div style="font-size:10px;font-weight:500">Lorem ipsum</div><div class="tiny" style="width:120px">Lorem ipsum dolor sit amet, consectetuer adipiscing elit.</div></div>
  <div style="left:376px;top:165px"><div style="font-size:10px;font-weight:500">Lorem ipsum</div><div class="tiny" style="width:120px">Lorem ipsum dolor sit amet, consectetuer adipiscing elit.</div></div>
  <div style="left:346px;top:238px"><div style="font-size:10px;font-weight:500">Lorem ipsum</div><div class="tiny" style="width:120px">Lorem ipsum dolor sit amet, consectetuer adipiscing elit.</div></div>
</section>

<!-- 12 project 01 -->
<section class="slide">
  <svg class="hdr" viewBox="0 0 555 312"><path d="M432 312V0H490C530 0 555 25 555 60V312Z" fill="var(--black)"/><path d="M360 0H470C440 0 420 20 420 50V312H360Z" fill="var(--white)"/></svg>
  <div class="photo" role="img" aria-label="Black and white photo of modern apartment buildings" style="left:361px;top:55px;width:159px;height:201px;border-top-left-radius:30px"></div>
  <div style="left:41px;top:58px;font-weight:700;font-size:20px;color:var(--black)">PROJECT 01</div>
  <div style="left:41px;top:90px;font-size:7px;letter-spacing:4px">SUBTITLE GOES HERE</div>
  <p class="body" style="left:41px;top:128px;width:278px;line-height:16.5px">Lorem ipsum dolor sit amet, consectetuer adipiscing elit, sed diam nonummy nibh euismod tincidunt ut laoreet dolore magna aliquam erat volutpat. Ut wisi enim ad minim veniam, quis nostrud exerci tation ullamcorper suscipit lobortis nisl ut aliquip ex ea commodo consequat. Duis autem vel eum iriure dolor in hendrerit in vulputate velit esse molestie consequat, vel illum dolore eu feugiat nulla facilisis at vero eros et accumsan et iusto odio dignissim qui blandit praesent luptatum zzril delenit augue duis dolore te feugait nulla facilisi.</p>
</section>

<!-- 13 management -->
<section class="slide">
  <div style="left:0;width:555px;top:12px;text-align:center;font-weight:700;font-size:16px;color:var(--black)">OUR MANAGEMENT</div>
  <div style="left:258px;top:36px;width:40px;height:2px;background:var(--red)"></div>
  <svg class="hdr" viewBox="0 0 555 312"><rect x="49" y="55" width="456" height="225" rx="16" fill="none" stroke="#999" stroke-dasharray="2 2"/>
    <g fill="none" stroke="var(--red)" stroke-dasharray="1.5 1.5"><path d="M208 125V170H171M212 125V244H171"/></g>
    <g fill="none" stroke="#777" stroke-dasharray="1.5 1.5"><path d="M348 125V153H378M352 125V190H378M356 125V228H378M360 125V266H378"/></g></svg>
  <div style="left:116px;top:63px;width:322px;height:62px;background:var(--black);border-radius:10px;box-shadow:0 4px 8px rgba(0,0,0,.3)"><div class="brand" style="text-align:center;font-size:26px;margin-top:17px">ZENITH</div></div>
  <div class="mgmt-box" style="left:67px;top:135px;width:104px;height:70px;line-height:70px;background:var(--red);color:var(--white)">Lorem ipsum</div>
  <div class="mgmt-box" style="left:67px;top:209px;width:104px;height:70px;line-height:70px;background:var(--red);color:var(--white)">Lorem ipsum</div>
  <div class="mgmt-box" style="left:227px;top:138px;width:106px;height:30px;line-height:30px;background:var(--white)">Lorem ipsum</div>
  <div class="mgmt-box" style="left:227px;top:175px;width:106px;height:30px;line-height:30px;background:var(--white)">Lorem ipsum</div>
  <div class="mgmt-box" style="left:227px;top:213px;width:106px;height:30px;line-height:30px;background:var(--white)">Lorem ipsum</div>
  <div class="mgmt-box" style="left:227px;top:251px;width:106px;height:30px;line-height:30px;background:var(--white)">Lorem ipsum</div>
  <div class="mgmt-box" style="left:378px;top:138px;width:106px;height:30px;line-height:30px;background:#9a9a9a;color:var(--white)">Lorem ipsum</div>
  <div class="mgmt-box" style="left:378px;top:175px;width:106px;height:30px;line-height:30px;background:#9a9a9a;color:var(--white)">Lorem ipsum</div>
  <div class="mgmt-box" style="left:378px;top:213px;width:106px;height:30px;line-height:30px;background:#9a9a9a;color:var(--white)">Lorem ipsum</div>
  <div class="mgmt-box" style="left:378px;top:251px;width:106px;height:30px;line-height:30px;background:#9a9a9a;color:var(--white)">Lorem ipsum</div>
</section>

<!-- 14 section break -->
<section class="slide">
  <div class="photo" role="img" aria-label="Black and white photo of a bright kitchen interior" style="left:0;top:0;width:555px;height:312px;background:linear-gradient(135deg,#cfcfcf,#f2f2f2 60%,#9c9c9c)"></div>
  <div style="left:43px;top:79px;width:304px;height:191px;background:var(--black);border-radius:16px"></div>
  <div style="left:67px;top:51px;width:311px;height:211px;border:1.5px solid var(--white);border-radius:16px"></div>
  <div class="brand" style="left:242px;top:102px;font-size:26px">ZENITH</div>
  <div style="left:82px;top:198px;color:var(--white);font-weight:700;font-size:20px">SECTION BREAK</div>
  <div style="left:82px;top:228px;width:48px;height:2px;background:var(--white)"></div>
</section>

<!-- 15 partners -->
<section class="slide">
  <svg class="hdr" viewBox="0 0 555 312"><path d="M0 0H490C482 32 468 50 440 50H50C20 50 0 70 0 100Z" fill="var(--black)"/></svg>
  <div class="hdr-title" style="left:43px">OUR PARTNERS</div>
  <div class="badge" style="left:88px;top:102px;width:80px;height:32px"><i></i></div>
  <div class="badge" style="left:186px;top:102px;width:81px;height:32px"><i></i></div>
  <div class="badge" style="left:284px;top:102px;width:80px;height:32px"><i></i></div>
  <div class="badge" style="left:382px;top:102px;width:81px;height:32px"><i></i></div>
  <div class="badge" style="left:88px;top:158px;width:80px;height:32px"><i></i></div>
  <div class="badge" style="left:186px;top:158px;width:81px;height:32px"><i></i></div>
  <div class="badge" style="left:284px;top:158px;width:80px;height:32px"><i></i></div>
  <div class="badge" style="left:382px;top:158px;width:81px;height:32px"><i></i></div>
  <div class="badge" style="left:88px;top:210px;width:80px;height:32px"><i></i></div>
  <div class="badge" style="left:186px;top:210px;width:81px;height:32px"><i></i></div>
  <div class="badge" style="left:284px;top:210px;width:80px;height:32px"><i></i></div>
  <div class="badge" style="left:382px;top:210px;width:81px;height:32px"><i></i></div>
</section>

<!-- 16 analysis -->
<section class="slide">
  <svg class="hdr" viewBox="0 0 555 312"><path d="M0 0H490C482 32 468 50 440 50H50C20 50 0 70 0 100Z" fill="var(--black)"/>
    <g fill="var(--red)"><circle cx="276" cy="136" r="36"/><circle cx="319" cy="179" r="36"/><circle cx="276" cy="222" r="36"/><circle cx="233" cy="179" r="36"/></g>
    <g fill="var(--black)"><circle cx="276" cy="136" r="22"/><circle cx="276" cy="222" r="22"/></g>
    <g fill="var(--white)"><circle cx="319" cy="179" r="22"/><circle cx="233" cy="179" r="22"/><circle cx="276" cy="136" r="20"/><circle cx="276" cy="222" r="20"/></g>
    <rect x="254" y="165" width="44" height="28" fill="var(--red)"/>
    <g font-family="Poppins,sans-serif" font-size="14" text-anchor="middle" fill="var(--black)"><text x="276" y="141">S</text><text x="319" y="184">W</text><text x="276" y="227">O</text><text x="233" y="184">T</text></g>
    <text x="276" y="182" font-family="Poppins,sans-serif" font-size="8" font-weight="800" text-anchor="middle" fill="var(--white)">ZENITH</text></svg>
  <div class="hdr-title">OUR ANALYSIS</div>
  <div style="left:20px;top:103px;width:172px;text-align:right"><div class="label red" style="font-size:7px">STRENGTH</div><div class="tiny" style="color:#444">Lorem ipsum dolor sit amet, consectetuer adipiscing elit, sed diam nonummy nibh euismod tincidunt ut laoreet dolore magna aliquam erat</div></div>
  <div style="left:359px;top:103px;width:172px"><div class="label red" style="font-size:7px">WEAKNESS</div><div class="tiny" style="color:#444">Lorem ipsum dolor sit amet, consectetuer adipiscing elit, sed diam nonummy nibh euismod tincidunt ut laoreet dolore magna aliquam erat</div></div>
  <div style="left:20px;top:220px;width:172px;text-align:right"><div class="label red" style="font-size:7px">THREAT</div><div class="tiny" style="color:#444">Lorem ipsum dolor sit amet, consectetuer adipiscing elit, sed diam nonummy nibh euismod tincidunt ut laoreet dolore magna aliquam erat</div></div>
  <div style="left:359px;top:220px;width:172px"><div class="label red" style="font-size:7px">OPPORTUNITY</div><div class="tiny" style="color:#444">Lorem ipsum dolor sit amet, consectetuer adipiscing elit, sed diam nonummy nibh euismod tincidunt ut laoreet dolore magna aliquam erat</div></div>
</section>

<!-- 17 icons -->
<section class="slide">
  <div style="left:0;width:555px;top:16px;text-align:center;font-weight:700;font-size:13px;color:var(--black)">FREE EDITABLE VECTOR ICON LINKS AVAILABLE</div>
  <div role="img" aria-label="Grid of editable line icons" style="left:27px;top:67px;width:503px;height:219px;background:linear-gradient(180deg,#e4e4e4,#d4d4d4);border-radius:4px"></div>
</section>

<!-- 18 thank you -->
<section class="slide">
  <svg class="hdr" viewBox="0 0 555 312"><path d="M0 312V200C0 180 12 168 32 168H380C400 168 405 150 420 150H555V312Z" fill="var(--black)"/><path d="M300 168C330 168 350 150 360 120" fill="none"/></svg>
  <div style="left:54px;top:42px;font-weight:700;font-size:22px;color:var(--black)">THANK YOU</div>
  <div style="left:54px;top:76px;width:56px;height:2px;background:var(--red)"></div>
  <div class="photo" role="img" aria-label="Black and white portrait of the presenter" style="left:360px;top:62px;width:120px;height:120px;border-radius:50%;border:4px solid var(--white)"></div>
  <div style="left:44px;top:167px;color:var(--white);font-weight:600;font-size:10px">PRESENTER NAME</div>
  <div style="left:42px;top:192px;display:flex;flex-direction:column;gap:10px">
    <div class="contact"><svg width="13" height="13" viewBox="0 0 24 24" fill="var(--white)"><path d="M6 2l4 4-2 3c1 3 4 6 7 7l3-2 4 4-3 4C10 22 2 14 2 5z"/></svg>+1 234 567 890</div>
    <div class="contact"><svg width="13" height="13" viewBox="0 0 24 24" fill="none" stroke="var(--white)" stroke-width="2"><circle cx="12" cy="12" r="10"/><path d="M2 12h20M12 2c4 4 4 16 0 20M12 2c-4 4-4 16 0 20"/></svg>www.yourwebsite.com</div>
    <div class="contact"><svg width="13" height="13" viewBox="0 0 24 24"><rect x="2" y="5" width="20" height="14" fill="var(--white)"/><path d="M2 5l10 8 10-8" stroke="var(--black)" stroke-width="2" fill="none"/></svg>addyouremail@here.com</div>
    <div class="contact"><svg width="13" height="13" viewBox="0 0 24 24" fill="var(--white)"><path d="M12 2a7 7 0 0 1 7 7c0 5-7 13-7 13S5 14 5 9a7 7 0 0 1 7-7z"/><circle cx="12" cy="9" r="2.5" fill="var(--black)"/></svg>Add your location here</div>
  </div>
  <div class="brand" style="left:355px;top:236px;font-size:32px">ZENITH</div>
</section>

</main>
</body>
</html>
```